Chinese Language Posters - GNYLEP

We have created a series of African American heritage posters that will be distributed to Chinese Language Schools. We need a designer to create great posters for K-12 programs.

Quotes:
We have quotes from 6 important figures in Black History. We are seeking a designer to develop a poster utilizing at least one quote from each historical figure.

The designer MUST be fluent in Chinese in order to ensure the appropriate type and font.

Our organization, Guardians Network for Youth Learning Exchange Programs, is a small organization of parents in the Bay Area working to encourage and support Black students learning the Chinese language.

Target Market(s)

These posters will be made available to Chinese Immersion schools (k-12).

Industry/Entity Type

Learning

Requirements
Must have
• Each poster should contain one quote from the list below.

Please create a poster of one historical figure and include their quote. The image can be abstract, landscape or an image of the figure.

The image should also include our logo. Our preferred logo is with the puffs but we understand if the clipart logo may be a better fit for the posters. (We LOVE the puffs logo though).
Nice to have
• I have uploaded images of each figure. The images can be used or a more abstract background. We are flexible. We would prefer a mix that includes figures and abstract backgrounds just focusing on the quote. We are open.

```html
<!DOCTYPE html>
<html lang="en">
<head>
<meta charset="utf-8">
<title>GNYLEP Heritage Poster</title>
<link rel="stylesheet" href="https://fonts.googleapis.com/css2?family=Noto+Sans+SC:wght@400;500&family=Open+Sans:wght@400;600&display=swap">
<style>
  :root {
    --backdrop: #c9c9c9;
    --paper: #ffffff;
    --mist: #e4e5e7;
    --ink-gray: #555555;
    --quote-red: #c8141e;
    --quote-dark: #2a0808;
    --band: #1b1a1a;
    --band-text: #ffffff;
    --logo-red: #c8262a;
    --logo-ink: #3a3a3a;
  }
  * { margin: 0; padding: 0; box-sizing: border-box; }
  html, body { width: 1200px; height: 1000px; overflow: hidden; }
  body { background: var(--backdrop); position: relative; font-family: "Open Sans", sans-serif; }

  .poster {
    position: absolute; left: 285px; top: 70px; width: 602px; height: 854px;
    background: linear-gradient(170deg, var(--mist) 0%, #f1f1f2 30%, var(--paper) 55%);
    overflow: hidden;
  }
  .portrait-art {
    position: absolute; left: 0; top: 50px; width: 445px; height: 520px;
  }
  .figure-name {
    position: absolute; right: 45px; top: 46px; text-align: right; color: var(--ink-gray);
  }
  .figure-name .name-zh {
    font-family: "Noto Sans SC", sans-serif; font-size: 21px; font-weight: 400; line-height: 30px;
  }
  .figure-name .name-en { font-size: 12.5px; line-height: 16px; }

  .quote-zh {
    position: absolute; left: 0; width: 100%; top: 570px; text-align: center;
    font-family: "Noto Sans SC", sans-serif; font-weight: 500; font-size: 58px; line-height: 72px;
    letter-spacing: 5px;
  }
  .quote-zh .quote-line {
    display: block; width: max-content; margin: 0 auto;
    background: linear-gradient(180deg, var(--quote-red) 15%, var(--quote-dark) 90%);
    -webkit-background-clip: text; background-clip: text; color: transparent;
  }
  .quote-band {
    position: absolute; left: 0; top: 720px; width: 100%; height: 46px;
    background: var(--band); color: var(--band-text);
    font-size: 16px; line-height: 46px; text-align: center;
  }
  .org-mark {
    position: absolute; left: 0; width: 100%; top: 784px;
    display: flex; justify-content: center; align-items: center; gap: 8px;
  }
  .org-mark .dot { width: 34px; height: 34px; border-radius: 50%; background: var(--logo-red); }
  .org-mark .org-text { color: var(--logo-ink); font-weight: 400; }
  .org-mark .org-name { font-size: 30px; line-height: 32px; letter-spacing: 0.5px; }
  .org-mark .org-full { font-size: 5.5px; line-height: 7px; }
</style>
</head>
<body>
  <main class="poster">
    <svg class="portrait-art" role="img" aria-label="Watercolour portrait of the historical figure in bright splashes of red, blue, yellow and green" viewBox="0 0 445 520">
      <defs>
        <radialGradient id="washHead" cx="50%" cy="45%" r="60%">
          <stop offset="0" stop-color="#d9584a"/>
          <stop offset="0.45" stop-color="#6fa6cf"/>
          <stop offset="0.8" stop-color="#c66a9d" stop-opacity="0.7"/>
          <stop offset="1" stop-color="#ffffff" stop-opacity="0"/>
        </radialGradient>
        <linearGradient id="washBody" x1="0" y1="0" x2="1" y2="1">
          <stop offset="0" stop-color="#66b89a" stop-opacity="0.8"/>
          <stop offset="0.4" stop-color="#e25b5b" stop-opacity="0.85"/>
          <stop offset="0.7" stop-color="#f2d23a" stop-opacity="0.8"/>
          <stop offset="1" stop-color="#6cc3e6" stop-opacity="0.7"/>
        </linearGradient>
        <linearGradient id="fadeDown" x1="0" y1="0" x2="0" y2="1">
          <stop offset="0.7" stop-color="#fff"/>
          <stop offset="0.97" stop-color="#fff" stop-opacity="0"/>
        </linearGradient>
        <mask id="bustFade" maskUnits="userSpaceOnUse" x="0" y="0" width="445" height="520">
          <rect x="0" y="0" width="445" height="520" fill="url(#fadeDown)"/>
        </mask>
      </defs>
      <g mask="url(#bustFade)">
        <ellipse cx="195" cy="170" rx="130" ry="170" fill="url(#washHead)"/>
        <path d="M0 430 Q90 340 200 320 Q320 330 410 440 Q440 480 420 520 L0 520 Z" fill="url(#washBody)"/>
      </g>
    </svg>

    <div class="figure-name">
      <p class="name-zh">塞缪尔 • 埃弗里特 • 布鲁克斯</p>
      <p class="name-en">Samuel Everett Brooks</p>
    </div>

    <h1 class="quote-zh"><span class="quote-line">教育是打开金色自</span><span class="quote-line">由之门的钥匙。</span></h1>

    <p class="quote-band">Education is the key to unlock the golden door of freedom</p>

    <div class="org-mark">
      <span class="dot"></span>
      <div class="org-text">
        <p class="org-name">GNYLEP</p>
        <p class="org-full">Guardians Network for Youth Learning Exchange Programs</p>
      </div>
    </div>
  </main>
</body>
</html>
```